Quorvilan Mobile App

We are in need of a design for a mobile application that delivers relevant content to users based on the profile that they enter and based on the answers that they enter in a daily health tracker. There also will be functionality that will allow a user to check the cost of a medical service/ procedure before going to the medical provider (could get a list of providers and costs after entering procedure, service or prescription in a search box). The content will be articles or information that our team will find/develop on a daily basis and put into a database that the app will pull off of. The profile needs to capture age, sex, ethinicity (optional) and then have a list of topics that the user can select to get daily updated information/content. These topics are: Diabetes, Heart Disease, Hypertension, COPD, Back Pain, Weight Management, Depression, Cancer, Wellness Plan. The final design should allow for users to receive helpful health care information every day based on their profile and the answers in the daily health tracker.

Medical

```html
<!DOCTYPE html>
<html lang="en">
<head>
<meta charset="utf-8">
<title>Quorvilan — Feed</title>
<link rel="stylesheet" href="https://fonts.googleapis.com/css2?family=Roboto:wght@300;400;500;700&display=swap">
<style>
  :root {
    --page-bg: #ecebe8;
    --brand-green: #43bd5f;
    --screen-bg: #e4e4e4;
    --card-bg: #ffffff;
    --title-ink: #1f1f1f;
    --body-ink: #7a7a7a;
    --heart-red: #d7262b;
    --xray-orange: #f39a0c;
    --health-green: #6cc62d;
    --services-blue: #2f8ad3;
    --tab-bg: #f7f7f8;
    --tab-ink: #9a9a9a;
    --tab-active: #43bd5f;
    --white: #ffffff;
  }
  * { box-sizing: border-box; margin: 0; padding: 0; }
  html, body {
    width: 1200px; height: 1000px; overflow: hidden;
    background: var(--page-bg);
    font-family: "Roboto", Arial, sans-serif;
  }
  .app-screen {
    position: absolute; left: 345px; top: 46px;
    width: 510px; height: 906px;
    background: var(--screen-bg);
    display: flex; flex-direction: column;
    overflow: hidden;
    box-shadow: 0 10px 40px rgba(0,0,0,.15);
  }
  .app-header { background: var(--brand-green); color: var(--white); }
  .status-bar {
    height: 32px; display: flex; align-items: center; justify-content: space-between;
    padding: 0 12px; font-size: 15px; font-weight: 400;
  }
  .status-carrier { display: flex; align-items: center; gap: 6px; }
  .signal-dots { display: flex; gap: 3px; }
  .signal-dots span { width: 8px; height: 8px; border-radius: 50%; background: var(--white); }
  .signal-dots span.empty { background: none; border: 1px solid var(--white); }
  .status-battery { display: flex; align-items: center; gap: 6px; }
  .battery { width: 30px; height: 14px; border: 1.5px solid var(--white); border-radius: 3px; padding: 1.5px; position: relative; }
  .battery::before { content: ""; display: block; width: 100%; height: 100%; background: var(--white); border-radius: 1px; }
  .battery::after { content: ""; position: absolute; right: -4px; top: 3px; width: 2px; height: 5px; background: var(--white); border-radius: 0 1px 1px 0; }
  .nav-bar {
    height: 72px; display: flex; align-items: center; justify-content: center; gap: 12px;
    padding-bottom: 6px;
  }
  .brand-mark { width: 22px; height: 22px; border-radius: 50%; background: var(--white); }
  .brand-name { font-size: 32px; font-weight: 700; letter-spacing: .5px; color: var(--white); }

  .feed { flex: 1; overflow: hidden; padding: 10px 12px 0; display: flex; flex-direction: column; gap: 10px; }
  .feed-card {
    background: var(--card-bg); height: 166px; flex: none;
    display: flex; padding: 22px 20px 18px 12px; gap: 14px;
  }
  .topic-badge { width: 112px; flex: none; display: flex; flex-direction: column; align-items: center; gap: 10px; }
  .topic-icon { width: 78px; height: 78px; border-radius: 50%; display: flex; align-items: center; justify-content: center; }
  .topic-label { font-size: 19px; font-weight: 400; }
  .topic-heart .topic-icon { background: var(--heart-red); }
  .topic-heart .topic-label { color: var(--heart-red); }
  .topic-xray .topic-icon { background: var(--xray-orange); }
  .topic-xray .topic-label { color: var(--xray-orange); }
  .topic-health .topic-icon { background: var(--health-green); }
  .topic-health .topic-label { color: var(--health-green); }
  .topic-services .topic-icon { background: var(--services-blue); }
  .topic-services .topic-label { color: var(--services-blue); }
  .article { flex: 1; padding-top: 6px; }
  .article-title { font-size: 20px; font-weight: 500; color: var(--title-ink); margin-bottom: 8px; line-height: 1.2; }
  .article-excerpt { font-size: 15.5px; font-weight: 300; color: var(--body-ink); line-height: 1.45; text-align: justify; }

  .tab-bar {
    height: 80px; background: var(--tab-bg); border-top: 1px solid #d8d8d8;
    display: flex; flex: none;
  }
  .tab { flex: 1; display: flex; flex-direction: column; align-items: center; justify-content: center; gap: 4px; color: var(--tab-ink); font-size: 13px; position: relative; }
  .tab-active { color: var(--tab-active); }
  .tab-active::after { content: ""; position: absolute; bottom: 4px; width: 28px; height: 2px; background: var(--heart-red); }
</style>
</head>
<body>
<main class="app-screen">
  <header class="app-header">
    <div class="status-bar">
      <div class="status-carrier">
        <div class="signal-dots"><span></span><span></span><span></span><span class="empty"></span><span class="empty"></span></div>
        <span>Nerva</span>
        <svg width="18" height="13" viewBox="0 0 18 13" aria-hidden="true"><path d="M9 12 L6 8.5 A4.5 4.5 0 0 1 12 8.5 Z M3.5 6 A8 8 0 0 1 14.5 6 L13 7.5 A6 6 0 0 0 5 7.5 Z M1 3.3 A12 12 0 0 1 17 3.3 L15.5 4.8 A10 10 0 0 0 2.5 4.8 Z" fill="#fff"/></svg>
      </div>
      <span class="status-time">4:21 PM</span>
      <div class="status-battery"><span>100%</span><div class="battery"></div></div>
    </div>
    <div class="nav-bar">
      <span class="brand-mark"></span>
      <span class="brand-name">Quorvilan</span>
    </div>
  </header>

  <section class="feed">
    <article class="feed-card">
      <div class="topic-badge topic-heart">
        <div class="topic-icon">
          <svg width="36" height="32" viewBox="0 0 36 32" aria-hidden="true"><path d="M18 29 C6 20 3 15 3 10 A7.5 7.5 0 0 1 18 7 A7.5 7.5 0 0 1 33 10 C33 15 30 20 18 29 Z" fill="none" stroke="#fff" stroke-width="2.5" stroke-linejoin="round"/></svg>
        </div>
        <span class="topic-label">Heart</span>
      </div>
      <div class="article">
        <h2 class="article-title">5 Exercises to Improve Heart Health</h2>
        <p class="article-excerpt">You don't need to be a hardcore athlete to boost your heart health. Moderate exercise can significantly reduce your risk of heart...</p>
      </div>
    </article>

    <article class="feed-card">
      <div class="topic-badge topic-xray">
        <div class="topic-icon">
          <svg width="34" height="34" viewBox="0 0 34 34" aria-hidden="true"><rect x="5" y="4" width="24" height="26" rx="2" fill="none" stroke="#fff" stroke-width="2.2"/><path d="M17 9 V25 M12 12 H22 M11 16 H23 M12 20 H22" stroke="#fff" stroke-width="1.8" stroke-linecap="round"/></svg>
        </div>
        <span class="topic-label">X-ray</span>
      </div>
      <div class="article">
        <h2 class="article-title">How X-rays Work</h2>
        <p class="article-excerpt">As with many of mankind's monumental discoveries, X-ray technology was invented completely by accident. In 1895, a Ger...</p>
      </div>
    </article>

    <article class="feed-card">
      <div class="topic-badge topic-health">
        <div class="topic-icon">
          <svg width="40" height="40" viewBox="0 0 40 40" aria-hidden="true"><g fill="none" stroke="#fff" stroke-width="2.2" stroke-linecap="round" stroke-linejoin="round"><path d="M8 20 H28 L31 17 H36 M31 23 H36 M31 17 V23"/><rect x="8" y="16" width="20" height="8" rx="1"/><path d="M3 20 H8 M13 16 V19 M17 16 V19 M21 16 V19"/></g></svg>
        </div>
        <span class="topic-label">Health</span>
      </div>
      <div class="article">
        <h2 class="article-title">2-day Free Health Services</h2>
        <p class="article-excerpt">In connection with the National Health Month, the City of ABCDE will hold a week-long free health services to all of its...</p>
      </div>
    </article>

    <article class="feed-card">
      <div class="topic-badge topic-services">
        <div class="topic-icon">
          <svg width="40" height="34" viewBox="0 0 40 34" aria-hidden="true"><g fill="none" stroke="#fff" stroke-width="2.2" stroke-linejoin="round"><path d="M4 24 V10 H24 V24 M24 14 H31 L36 20 V24 H4"/><circle cx="11" cy="26" r="3"/><circle cx="29" cy="26" r="3"/><path d="M14 13 V21 M10 17 H18" stroke-linecap="round"/></g></svg>
        </div>
        <span class="topic-label">Services</span>
      </div>
      <div class="article">
        <h2 class="article-title">Sample T</h2>
        <p class="article-excerpt">In connection with the National Health Month, the City of ABCDE will hold a week-long free health services to all of its...</p>
      </div>
    </article>
  </section>

  <nav class="tab-bar">
    <div class="tab tab-active">
      <svg width="30" height="28" viewBox="0 0 30 28" aria-hidden="true"><g fill="currentColor"><circle cx="4" cy="4" r="2.2"/><circle cx="4" cy="11" r="2.2"/><circle cx="4" cy="18" r="2.2"/><circle cx="4" cy="25" r="2.2"/><rect x="10" y="3" width="18" height="2"/><rect x="10" y="10" width="18" height="2"/><rect x="10" y="17" width="18" height="2"/><rect x="10" y="24" width="18" height="2"/></g></svg>
      <span>Feed</span>
    </div>
    <div class="tab">
      <svg width="28" height="28" viewBox="0 0 28 28" aria-hidden="true"><g fill="none" stroke="currentColor" stroke-width="1.8"><rect x="3" y="3" width="22" height="22"/><path d="M7 9 H21 M7 14 H21 M7 19 H21"/></g></svg>
      <span>Topics</span>
    </div>
    <div class="tab">
      <svg width="28" height="28" viewBox="0 0 28 28" aria-hidden="true"><g fill="none" stroke="currentColor" stroke-width="1.8"><circle cx="14" cy="14" r="11"/><circle cx="14" cy="11" r="4"/><path d="M7 21 C9 17 19 17 21 21"/></g></svg>
      <span>Profile</span>
    </div>
    <div class="tab">
      <svg width="32" height="28" viewBox="0 0 32 28" aria-hidden="true"><g fill="none" stroke="currentColor" stroke-width="1.8"><circle cx="6" cy="14" r="3.5"/><circle cx="16" cy="14" r="3.5"/><circle cx="26" cy="14" r="3.5"/></g></svg>
      <span>More</span>
    </div>
  </nav>
</main>
</body>
</html>
```